Scandinavian Online Sewing store need a flier

We need a 'flier' or over sized business card to include with orders which are shipped to customers. We are based in Norway and looking for something which will appeal to the Scandinavian market. The business name is 'Trådloftet' which in English means 'sewing cupboard'.

We are aiming for the younger market sector and stocking 'fresher' and 'younger' fabric, patterns and notions. (See Stitch the lot, Harlan+B, Quill & Tarrow, Velbrune K etc.)

We would like a A5/A6 sized card which we could use in place of a business card. It should include the logo and perhaps a textured background (either paper or fabric).

Looking forward to see the ideas of all you amazingly creative souls!

Target Market(s)

Scandinavian home sewers who are interested in creating and design

Industry/Entity Type

Textile

Requirements
Must have
• logo (Attached to project) picture or artwork
Nice to have
• texture background

```html
<!DOCTYPE html>
<html lang="no">
<head>
<meta charset="utf-8">
<title>Trådloftet – flier</title>
<link rel="stylesheet" href="https://fonts.googleapis.com/css2?family=Cherry+Swash:wght@700&family=Montserrat:wght@500;700&display=swap">
<style>
  :root {
    --page-bg: #e9e6e2;
    --card-bg: #f1f1ef;
    --card-weave: rgba(0, 0, 0, 0.035);
    --stitch: #4a4a4a;
    --ink: #1d1d1f;
    --moss: #4b5a2c;
    --sage: #b5cc8a;
    --cupboard-red: #b84444;
    --cupboard-dark: #3a1c1c;
    --rule: #6b6b6b;
  }
  * { margin: 0; padding: 0; box-sizing: border-box; }
  html, body {
    width: 1200px;
    height: 1000px;
    overflow: hidden;
    background: var(--page-bg);
  }
  .canvas {
    position: relative;
    width: 1200px;
    height: 1000px;
  }
  .card {
    position: absolute;
    left: 110px;
    top: 150px;
    width: 980px;
    height: 698px;
    background-color: var(--card-bg);
    background-image:
      repeating-linear-gradient(0deg, var(--card-weave) 0 1px, transparent 1px 3px),
      repeating-linear-gradient(90deg, var(--card-weave) 0 1px, transparent 1px 3px);
  }
  .card__stitching {
    position: absolute;
    left: 20px;
    top: 25px;
    right: 20px;
    bottom: 18px;
    border: 1.5px dashed var(--stitch);
  }
  .brand__mark {
    position: absolute;
    left: 237px;
    top: 105px;
    width: 125px;
    height: 185px;
    background: var(--sage);
  }
  .brand__name {
    position: absolute;
    left: 40px;
    top: 316px;
    width: 520px;
    text-align: center;
    font-family: "Montserrat", sans-serif;
    font-weight: 500;
    font-size: 46px;
    line-height: 48px;
    letter-spacing: 0.26em;
    text-indent: 0.26em;
    color: var(--ink);
  }
  .rule {
    position: absolute;
    left: 87px;
    width: 426px;
    border-top: 2px dotted var(--rule);
  }
  .rule--top { top: 389px; }
  .rule--bottom { top: 554px; }
  .tagline {
    position: absolute;
    left: 20px;
    top: 402px;
    width: 560px;
    text-align: center;
    font-family: "Cherry Swash", serif;
    font-weight: 700;
    font-size: 44px;
    line-height: 70px;
    color: var(--moss);
  }
  .web {
    position: absolute;
    left: 60px;
    top: 582px;
    width: 480px;
    text-align: center;
    font-family: "Montserrat", sans-serif;
    font-weight: 700;
    font-size: 20px;
    line-height: 26px;
    color: var(--ink);
  }
  .cupboard {
    position: absolute;
    left: 605px;
    top: 75px;
    width: 315px;
    height: 580px;
    background: linear-gradient(135deg, var(--cupboard-red), var(--cupboard-dark));
  }
</style>
</head>
<body>
<main class="canvas">
  <section class="card">
    <div class="card__stitching"></div>

    <span class="brand__mark"></span>
    <h1 class="brand__name">TRÅDLOFTET</h1>
    <div class="rule rule--top"></div>
    <p class="tagline">“Fristelser for de som<br>elsker å skaper”</p>
    <div class="rule rule--bottom"></div>
    <p class="web">www.tradloftet.no</p>

    <div class="cupboard" role="img" aria-label="Illustration of a red kitchen cupboard stitched on as a fabric patch"></div>
  </section>
</main>
</body>
</html>
```